Stationery & business cards for nonprofit
WELL Wells of kindness beyond measure
Stationery & business cards for nonprofit - Religion and Spirituality
Creative Brief
Use same font as used in my logo
Ruth Pelling
President
481 Orchard Lane Birmingham, AL 35187
ruth@wellkb.org
www.wellkb.org
We are open to ideas and suggestions using our logo, this is a nonprofit that supports an orphanage and assists widows in Africa, as shown in the earth tone in the logo. Logo information: Font: Desire (manipulated), Swiss Condensed, Times Roman Color: Pantone 1395, Pantone 7407, Pantone 364 Our website is currently under development, but you can see pictures, etc to get a feel for our nonprofit by going to www.wellkb.org
We are thinking to put just the logo on the back of the card with the name (wells of kindness beyond measure) and the verse listed - I John 3:16-18
mirabelcostow mirabelcostow
AI and EPS file formats have been uploaded for use as needed.

```html
<!DOCTYPE html>
<html lang="en">
<head>
<meta charset="utf-8">
<title>WELL – Business Card</title>
<link href="https://fonts.googleapis.com/css2?family=Michroma&family=Arimo:wght@400;700&display=swap" rel="stylesheet">
<style>
  :root{
    --bg:#5b5b5b;
    --paper:#ffffff;
    --paper-shade:#e4e4e4;
    --gold:#b8903a;
    --gold-dark:#8d6a22;
    --gold-light:#d4b266;
    --green:#3c7d1c;
    --green-light:#6aa12a;
    --silver:#c9c9c9;
    --black:#1c1c1c;
    --ink:#222222;
    --white:#ffffff;
  }
  html,body{margin:0;padding:0;width:1200px;height:904px;overflow:hidden;background:var(--bg);}
  .canvas{position:relative;width:1200px;height:904px;}
  .card{position:absolute;width:560px;height:320px;overflow:hidden;box-shadow:0 6px 18px rgba(0,0,0,.35);}
  .card-front{left:60px;top:120px;background:linear-gradient(180deg,var(--paper) 0%,var(--paper-shade) 100%);}
  .card-back{left:580px;top:470px;background:var(--gold);}
  .card svg.waves{position:absolute;inset:0;width:100%;height:100%;}

  .logo{position:absolute;display:flex;align-items:center;gap:8px;}
  .logo-mark{width:14px;height:14px;border-radius:50%;}
  .logo-name{font-family:"Michroma",sans-serif;font-size:38px;letter-spacing:2px;line-height:1;}
  .logo-tagline{font-family:"Arimo",sans-serif;font-size:9px;font-weight:700;margin-top:4px;}
  .card-front .logo{left:22px;top:30px;flex-direction:column;align-items:flex-start;gap:0;}
  .card-front .logo-row{display:flex;align-items:center;gap:8px;}
  .card-front .logo-mark{background:var(--gold);}
  .card-front .logo-name{color:var(--gold);}
  .card-front .logo-tagline{color:var(--green);}

  .card-back .logo{left:200px;top:175px;flex-direction:column;align-items:flex-start;gap:0;}
  .card-back .logo-row{display:flex;align-items:center;gap:8px;}
  .card-back .logo-mark{background:var(--white);}
  .card-back .logo-name{color:var(--white);}
  .card-back .logo-tagline{color:var(--white);}

  .person{position:absolute;right:26px;top:152px;text-align:left;font-family:"Arimo",sans-serif;color:var(--ink);}
  .person-name{font-size:17px;letter-spacing:.5px;}
  .person-title{font-size:8px;letter-spacing:.3px;margin-top:2px;}

  .contact-list{position:absolute;left:16px;top:224px;margin:0;padding:0;list-style:none;font-family:"Arimo",sans-serif;font-size:8px;color:var(--white);}
  .contact-list li{display:flex;align-items:center;gap:7px;height:17px;}
  .contact-list svg{width:9px;height:9px;fill:var(--white);}

  .address{position:absolute;right:26px;top:236px;font-family:"Michroma",sans-serif;font-size:10px;line-height:18px;color:var(--white);}
</style>
</head>
<body>
<div class="canvas">

  <section class="card card-front" aria-label="Business card front">
    <svg class="waves" viewBox="0 0 560 320" preserveAspectRatio="none" aria-hidden="true">
      <defs>
        <linearGradient id="goldFront" x1="0" y1="0" x2="1" y2="1">
          <stop offset="0" stop-color="var(--gold-light)"/>
          <stop offset=".5" stop-color="var(--gold)"/>
          <stop offset="1" stop-color="var(--gold-dark)"/>
        </linearGradient>
        <linearGradient id="silverFront" x1="0" y1="0" x2="1" y2="0">
          <stop offset="0" stop-color="#ffffff"/>
          <stop offset="1" stop-color="#8e8e8e"/>
        </linearGradient>
      </defs>
      <path d="M0 158 C120 150 220 205 360 175 S500 125 560 132 L560 150 C500 145 420 190 340 200 C230 212 130 175 0 178Z" fill="var(--green)"/>
      <path d="M300 185 C400 170 480 130 560 138 L560 158 C480 150 410 195 320 200Z" fill="url(#silverFront)"/>
      <path d="M0 176 C130 172 230 215 340 202 C430 192 490 152 560 156 L560 320 L0 320Z" fill="url(#goldFront)"/>
    </svg>

    <div class="logo">
      <div class="logo-row"><span class="logo-name">WELL</span><span class="logo-mark"></span></div>
      <div class="logo-tagline">Wells of kindness beyond measure</div>
    </div>

    <div class="person">
      <div class="person-name">RUTH PELLING</div>
      <div class="person-title">MANAGING DIRECTOR</div>
    </div>

    <ul class="contact-list">
      <li><svg viewBox="0 0 10 10"><path d="M2 0.5 L3.8 2.6 L2.8 3.6 Q4 6 6.4 7.2 L7.4 6.2 L9.5 8 L8.3 9.5 Q3 9 0.5 1.7Z"/></svg>205 555 0143</li>
      <li><svg viewBox="0 0 10 10"><rect x="2.5" y="0.5" width="5" height="9" rx="1"/></svg>205 555 0144</li>
      <li><svg viewBox="0 0 10 10"><rect x="0.5" y="2" width="9" height="7" rx="1"/></svg>205 555 0145</li>
      <li><svg viewBox="0 0 10 10"><path d="M0.5 2 H9.5 V8.5 H0.5Z M0.5 2 L5 5.5 L9.5 2"/></svg>ruth@wellkb.org</li>
      <li><svg viewBox="0 0 10 10"><circle cx="5" cy="5" r="4.5"/></svg>www.wellkb.org</li>
    </ul>

    <div class="address">481 Orchard Lane<br>Birmingham, AL 35187</div>
  </section>

  <section class="card card-back" aria-label="Business card back">
    <svg class="waves" viewBox="0 0 560 320" preserveAspectRatio="none" aria-hidden="true">
      <defs>
        <linearGradient id="goldBack" x1="0" y1="0" x2="1" y2="1">
          <stop offset="0" stop-color="var(--gold-light)"/>
          <stop offset="1" stop-color="var(--gold-dark)"/>
        </linearGradient>
        <linearGradient id="silverBack" x1="0" y1="0" x2="1" y2="0">
          <stop offset="0" stop-color="#8e8e8e"/>
          <stop offset=".5" stop-color="#ffffff"/>
          <stop offset="1" stop-color="#9a9a9a"/>
        </linearGradient>
      </defs>
      <rect width="560" height="320" fill="url(#goldBack)"/>
      <path d="M0 128 C150 110 250 150 380 118 S510 78 560 86 L560 100 C500 96 430 140 360 146 C250 160 130 130 0 150Z" fill="url(#silverBack)"/>
      <path d="M0 146 C120 132 230 160 340 150 C430 142 490 108 560 100 L560 112 C490 118 430 160 340 164 C220 170 110 150 0 160Z" fill="var(--green)"/>
      <path d="M0 158 C110 150 220 172 340 162 C430 156 490 118 560 110 L560 320 L0 320Z" fill="var(--black)"/>
    </svg>

    <div class="logo">
      <div class="logo-row"><span class="logo-name">WELL</span><span class="logo-mark"></span></div>
      <div class="logo-tagline">Wells of kindness beyond measure</div>
    </div>
  </section>

</div>
</body>
</html>
```